Amazing Looking Flyer for Moving Services

This project is a bit special, so please read carefully.
I'm working with new online design system Plivora and need good designs based on that system.
You will be redesigning the attached ad/flyer using Plivora.
Here is my starting design but please do not use it because it didn't start good:
https://beta2.plivora-example.com/pub/tobiasm/DeskTidying

Please create the flyer in the size 1275x1650 pixels, for email and PDF and website.
This needs to be designed with Plivora so I can change it later.
You will need to register at plivora-example.com for this job but use only the free version there, do not pay for images or leave them watermarked and I'll pay later.

No logo is needed. Only text, better layout and some pictures.
Pictures can be from Plivora, or you can create some vector graphics, as I don't want to pay for other stock photos.

Note: when you do anything in Plivora you can click Publish, and after I choose and pay for design then you can publish again with option to make it editable by anyone. Then I will be able to take it and edit myself later.

Industry/Entity Type

Online

Requirements
Must have
• some graphics
• must be done in plivora for my editing later

```html
<!DOCTYPE html>
<html lang="en">
<head>
<meta charset="utf-8">
<title>Cartwell Moving Flyer</title>
<link href="https://fonts.googleapis.com/css2?family=Exo+2:ital,wght@1,900&family=Archivo:wght@700;800&display=swap" rel="stylesheet">
<style>
  :root {
    --stage: #7fd0d6;
    --paper: #e6f4fb;
    --sky: #c6e8f7;
    --wave: #8fd3f2;
    --blue: #2bb3e8;
    --deep-blue: #1a7fc0;
    --navy: #0f1a2e;
    --red: #ee1c24;
    --grey: #4a4a4a;
    --white: #ffffff;
  }
  * { margin: 0; padding: 0; box-sizing: border-box; }
  html, body { width: 1200px; height: 1000px; overflow: hidden; }
  body { background: var(--stage); position: relative; font-family: "Archivo", Arial, sans-serif; }

  .flyer {
    position: absolute; left: 248px; top: 43px;
    width: 707px; height: 915px;
    background: var(--paper);
    overflow: hidden;
    box-shadow: 0 2px 6px rgba(0,0,0,.25);
    color: var(--navy);
  }
  .flyer-art { position: absolute; inset: 0; }

  .headline {
    position: absolute; left: 36px; top: 42px;
    font-family: "Exo 2", Arial, sans-serif; font-style: italic; font-weight: 900;
    font-size: 58px; line-height: 1; color: #050505; letter-spacing: .5px;
    white-space: nowrap; transform: scaleX(1.22); transform-origin: left top;
  }
  .tagline, .service-title {
    position: absolute; font-family: "Exo 2", Arial, sans-serif; font-style: italic;
    font-weight: 900; color: var(--red); letter-spacing: 1px;
    white-space: nowrap; transform: scaleX(1.36); transform-origin: left top;
  }
  .tagline { left: 34px; top: 98px; font-size: 27px; line-height: 30px; }

  .section-title { position: absolute; font-weight: 800; font-size: 21px; line-height: 30px; letter-spacing: .4px; }
  .free-title { left: 34px; top: 153px; }
  .move-title { left: 34px; top: 500px; }

  .list { position: absolute; list-style: none; font-weight: 700; font-size: 18px; line-height: 25px; letter-spacing: .3px; }
  .list li::before { content: "• "; font-size: 13px; }
  .free-list { left: 32px; top: 227px; }
  .move-list { left: 32px; top: 537px; display: grid; grid-template-columns: 138px auto; }

  .prices { position: absolute; left: 34px; top: 603px; font-weight: 800; font-size: 19px; line-height: 25px; letter-spacing: .4px; }
  .labor-note { position: absolute; left: 34px; top: 695px; font-weight: 700; font-size: 12.5px; line-height: 16.5px; }

  .service-title { left: 34px; top: 769px; font-size: 27px; line-height: 33px; }

  .contact { position: absolute; font-weight: 800; font-size: 18.5px; line-height: 30px; letter-spacing: .3px; }
  .services-list { left: 32px; top: 839px; }
  .phone-block { left: 342px; top: 839px; }

  .band {
    position: absolute; left: 372px; width: 335px; height: 24px;
    background: var(--blue); color: var(--white);
    font-weight: 800; font-size: 14.5px; line-height: 24px; padding-left: 20px;
    white-space: nowrap;
    text-shadow: 0 1px 1px rgba(0,0,0,.5);
  }
  .band-drive { top: 344px; }
  .band-best { top: 393px; }
</style>
</head>
<body>
<main class="flyer">
  <svg class="flyer-art" width="707" height="915" viewBox="0 0 707 915">
    <defs>
      <linearGradient id="photoTone" x1="0" y1="0" x2="0" y2="1">
        <stop offset="0" stop-color="#b9cfe0"/>
        <stop offset=".35" stop-color="#8fa08a"/>
        <stop offset=".55" stop-color="#d1552f"/>
        <stop offset=".75" stop-color="#4b4b4b"/>
        <stop offset="1" stop-color="#3a3a3a"/>
      </linearGradient>
      <linearGradient id="waveTone" x1="0" y1="0" x2="1" y2="1">
        <stop offset="0" stop-color="#2aa9e4"/>
        <stop offset="1" stop-color="#7fd0f3"/>
      </linearGradient>
    </defs>
    <circle class="soft-swirl" cx="60" cy="120" r="220" fill="#f2f9fd"/>
    <path class="soft-swirl" d="M380 0 C560 40 700 120 707 200 L707 0 Z" fill="#cfe9f7"/>
    <path class="arc-red" d="M707 150 C560 200 430 300 380 460 L405 470 C450 330 570 235 707 195 Z" fill="var(--red)"/>
    <path class="arc-grey" d="M707 78 C540 120 400 260 360 470 L372 472 C415 275 550 140 707 92 Z" fill="var(--grey)"/>
    <path class="truck-photo" role="img" aria-label="Photo of a moving truck on a highway" d="M707 270 L707 830 C590 700 470 560 400 470 C430 380 560 300 707 270 Z" fill="url(#photoTone)"/>
    <path class="wave-light" d="M0 440 C150 400 320 430 400 470 C520 600 650 760 707 915 L0 915 Z" fill="var(--sky)"/>
    <path class="wave-main" d="M0 338 C200 320 330 410 420 520 C520 650 600 760 620 915 L540 915 C520 760 440 620 360 540 C260 440 120 420 0 440 Z" fill="url(#waveTone)"/>
    <path class="wave-deep" d="M0 455 C180 420 330 500 430 600 C500 670 530 740 545 790 C510 720 440 640 350 570 C250 495 120 475 0 490 Z" fill="var(--deep-blue)"/>
    <path class="wave-pale" d="M0 520 C160 480 320 560 420 680 C480 760 520 840 530 915 L0 915 Z" fill="#b7e2f5"/>
    <circle class="wave-pale" cx="120" cy="640" r="150" fill="#a9dbf2" opacity=".5"/>
    <rect class="dolly-art" role="img" aria-label="Illustration of a hand truck loaded with cardboard boxes" x="345" y="160" width="150" height="135" rx="8" fill="#c9b89a" opacity=".85"/>
    <rect class="mover-art" role="img" aria-label="Cartoon of a mover carrying a house on his back" x="168" y="255" width="145" height="180" rx="10" fill="#8fae6a" opacity=".85"/>
  </svg>

  <h1 class="headline">Cartwell Moving</h1>
  <p class="tagline">We Are Here to Move Your Stuff</p>

  <h2 class="section-title free-title">We Provide The Following<br>At No Charge :</h2>
  <ul class="list free-list">
    <li>Blankets</li>
    <li>Dollies</li>
    <li>Tools</li>
  </ul>

  <p class="band band-drive">We Will Drive Anywhere Within Vegas</p>
  <p class="band band-best">The Best Movers in Las Vegas</p>

  <h2 class="section-title move-title">We Move :</h2>
  <ul class="list move-list">
    <li>Homes</li>
    <li>Offices</li>
    <li>Apartments</li>
    <li>And Storage</li>
  </ul>

  <p class="prices">2 Movers + Truck = $46.99<br>3 Movers + Truck = $66.99<br>4 Movers + Truck = $86.99</p>
  <p class="labor-note">Labor only = $19.99/hr per Mover<br>Customer Drive the truck from point<br>A to point B</p>

  <h2 class="service-title">We Provide Professional<br>Moving Service</h2>

  <p class="contact services-list">Loading And Unloading<br>Packing And Unpacking</p>
  <p class="contact phone-block">Call 702-555-0148<br>Available 24/7</p>
</main>
</body>
</html>
```